Stationery Design Project

We are interested in A4 paper letterheads, envelopes, maybe A4 folders where we can put the patients' results in and businesscards. No information will be given out for the time being.
We would like to see mainly shades of white.. please refer to
http://en.brivola.org/wiki/Category:Tints_of_pale
anti-flash white, splashed white,ghost white, ivory, snow and white smoke or even light grey
we are interested mainly on the silver design but we welcome the other colors as well. Since its about a gynecologist please avoid dark colors, instead use shades of beige, light grey and white

```html
<!DOCTYPE html>
<html lang="en">
<head>
<meta charset="utf-8">
<title>Business Card – Front and Back</title>
<link href="https://fonts.googleapis.com/css2?family=Arimo:wght@400;700&display=swap" rel="stylesheet">
<style>
  :root {
    --backdrop: #efede9;
    --card-white: #ffffff;
    --pale-grey: #dedcd7;
    --silver: #b9bbbd;
    --silver-deep: #9a9da0;
    --ink: #4a4f53;
    --rule: #a5a9ac;
  }
  * { box-sizing: border-box; margin: 0; padding: 0; }
  html, body {
    width: 1200px; height: 402px; overflow: hidden;
    background: var(--backdrop);
    font-family: "Arimo", Arial, sans-serif;
  }
  .sheet { position: relative; width: 1200px; height: 402px; }
  .card {
    position: absolute; top: 56px; width: 512px; height: 292px; overflow: hidden;
    box-shadow: 0 1px 4px rgba(0,0,0,.16);
  }
  .card--front { left: 64px; background: var(--card-white); }
  .card--back { left: 629px; background: var(--pale-grey); }

  .brand {
    position: absolute; left: 0; right: 0; display: flex; align-items: center; justify-content: center; gap: 10px;
    font-weight: 700; letter-spacing: .5px; color: var(--silver-deep);
  }
  .brand__dot { border-radius: 50%; background: var(--silver-deep); }
  .card--front .brand { top: 58px; font-size: 26px; }
  .card--front .brand__dot { width: 18px; height: 18px; }
  .card--back .brand { top: 104px; font-size: 34px; color: var(--ink); }
  .card--back .brand__dot { width: 22px; height: 22px; background: var(--ink); }

  .address {
    position: absolute; right: 302px; top: 170px; text-align: right; font-style: normal;
    font-size: 13.5px; line-height: 17px; color: var(--ink);
  }
  .divider { position: absolute; left: 233px; top: 163px; width: 1px; height: 60px; background: var(--rule); }
  .contacts {
    position: absolute; left: 260px; top: 167px; list-style: none;
    font-size: 13.5px; line-height: 18px; color: var(--ink);
  }
  .contacts li { display: flex; align-items: center; gap: 6px; }
  .contacts svg { width: 11px; height: 11px; fill: var(--ink); }

  .band { position: absolute; left: 0; bottom: 0; width: 512px; height: 62px; }
  .signature {
    position: absolute; left: 0; right: 0; bottom: 11px; display: flex; justify-content: center; align-items: baseline;
    color: var(--ink); font-size: 12.5px;
  }
  .signature strong { font-size: 15px; margin-right: 4px; }
  .signature .sep { width: 1px; height: 14px; background: var(--ink); margin: 0 9px; align-self: center; }

  .website {
    position: absolute; left: 0; right: 0; top: 248px; text-align: center;
    font-size: 14.5px; color: var(--ink);
  }
</style>
</head>
<body>
<main class="sheet">
  <section class="card card--front" aria-label="Card front">
    <div class="brand"><span class="brand__dot"></span>Pale Clinic</div>

    <address class="address">
      Street Name<br>City Name<br>State Zip Code
    </address>
    <span class="divider"></span>
    <ul class="contacts">
      <li><svg viewBox="0 0 12 12"><path d="M3 1l2 2.5-1.2 1.2a6 6 0 0 0 3.5 3.5L8.5 7 11 9l-1.3 1.8C5.5 10.5 1.5 6.5 1.2 2.3z"/></svg>123-456-7890</li>
      <li><svg viewBox="0 0 12 12"><rect x="3" y="0.5" width="6" height="11" rx="1"/><rect x="4" y="2" width="4" height="5" fill="#fff"/></svg>987-654-3210</li>
      <li><svg viewBox="0 0 12 12"><rect x="0.5" y="2.5" width="11" height="7"/><path d="M1 3l5 3.5L11 3" stroke="#fff" fill="none"/></svg>info@paleclinic.com</li>
    </ul>

    <svg class="band" viewBox="0 0 512 62" preserveAspectRatio="none" aria-hidden="true">
      <path d="M0 22 Q256 -4 512 24 L512 27 Q256 2 0 26z" fill="var(--silver)"/>
      <path d="M0 30 Q256 6 512 30 L512 62 L0 62z" fill="var(--pale-grey)"/>
    </svg>
    <p class="signature"><strong>Dr. Name,</strong> Gynecologist<span class="sep"></span>License No. XY 123456</p>
  </section>

  <section class="card card--back" aria-label="Card back">
    <div class="brand"><span class="brand__dot"></span>Pale Clinic</div>
    <p class="website">www.PaleClinic.Com</p>
  </section>
</main>
</body>
</html>
```